Dynamic Templates

Our company hosts web stores for our clients. They can set up as many as they wish on our platform, and select from the stock templates we provide. We are looking to increase the number of available stock templates.

Because our users can dynamically control many of the template elements - specifically colors - they have to be flexible and abide by certain rules. These rules are spelled out in the attached documents.

Here are links to two of our most used templates:
http://brivelta.tondashop.example/
http://quillorn.tondashop.example/

Templates need to have a landing page (what you see when first clicking one of the above links). There also needs to be a category page (what you see when clicking any category) and a product detail page (what you see when you arrive at an individual product, where there are various cart options like Buy Now or Request Info).

```html
<!DOCTYPE html>
<html lang="en">
<head>
<meta charset="utf-8">
<title>Tailgate Tote Cooler – Product Detail</title>
<link href="https://fonts.googleapis.com/css2?family=Didact+Gothic&display=swap" rel="stylesheet">
<style>
:root{
  --sky-light:#c4ecfb;
  --sky-mid:#9fcfe2;
  --sky-dark:#5a8ea3;
  --steel:#1f3340;
  --gray-light:#d9d9d9;
  --panel:#ffffff;
  --side:#f7f7f7;
  --ink:#111111;
  --navy:#14146a;
  --link:#1010c0;
  --logo:#2b2b2b;
  --tag:#8a8a8a;
}
*{box-sizing:border-box;margin:0;padding:0}
html,body{width:1200px;height:960px;overflow:hidden}
body{position:relative;font-family:"Didact Gothic",sans-serif;color:var(--ink);background:var(--gray-light)}
.header{position:absolute;left:0;top:0;width:1200px;height:108px;
  background:linear-gradient(to bottom,#8fbfd3 0%,var(--sky-light) 40%,var(--sky-light) 78%,var(--sky-dark) 94%,var(--steel) 100%)}
.logo{position:absolute;left:130px;top:4px;font-size:47px;color:var(--logo);text-shadow:2px 3px 3px rgba(0,0,0,.35);letter-spacing:.5px}
.tagline{position:absolute;left:131px;top:56px;font-size:23px;color:var(--tag);text-shadow:1px 2px 2px rgba(0,0,0,.3)}
.stage{position:absolute;left:0;top:108px;width:1200px;height:640px;background:linear-gradient(to bottom,#d4d4d4,#a9a9a9)}
.sidebar{position:absolute;left:128px;top:108px;width:203px;height:640px;background:var(--side);border-left:1px solid #555;border-right:1px solid #555;overflow:hidden}
.nav{list-style:none;margin-top:44px}
.nav li{height:28.8px;border-bottom:1px solid var(--navy);text-align:center;font-size:13px;color:var(--navy);line-height:20px;padding-top:2px}
.contact-bar{position:absolute;right:137px;top:115px;font-size:13px}
.contact-bar b{font-weight:bold}
.contact-bar em{font-style:italic}
.contact-bar a{color:var(--link);text-decoration:none}
.content{position:absolute;left:331px;top:160px;width:749px;height:588px;background:var(--panel);border-top:1px solid #333;border-right:1px solid #555;box-shadow:-3px 0 6px rgba(0,0,0,.25)}
.title{position:absolute;left:69px;top:3px;font-size:20px;font-weight:normal}
.continue{position:absolute;right:15px;top:5px;font-size:14px;color:var(--ink);text-decoration:underline}
.photo{position:absolute;left:68px;top:52px;width:237px;height:238px;border:1px solid #333;border-radius:6px;box-shadow:1px 2px 3px rgba(0,0,0,.4);background:#fff;padding:20px 22px}
.photo .fill{width:100%;height:100%;border-radius:4px;background:radial-gradient(ellipse at 50% 55%,#3a3a3a 0%,#6e6e6e 45%,#d8d8d8 75%,#fff 100%)}
.pricing{position:absolute;left:72px;top:296px;width:257px}
.pricing .heads{display:flex;justify-content:space-between}
.pricing .heads span{width:126px;text-align:center;font-size:19px;border-bottom:1px solid #222;padding-bottom:1px}
.pricing .rows{display:flex;justify-content:space-between;margin-top:15px;font-size:12px;line-height:14px}
.pricing .rows div{width:126px;text-align:center}
.actions{position:absolute;left:146px;top:405px}
.btn{display:flex;align-items:center;width:108px;height:22px;margin-bottom:4px;border-radius:11px;background:linear-gradient(#555,#111 60%,#000);color:#fff;font-size:10.5px;letter-spacing:.3px;padding-left:9px;position:relative;font-weight:bold}
.btn .ico{position:absolute;right:0;top:1px;width:20px;height:20px;border-radius:50%;background:#e8f0f6;border:1px solid #888}
.btn .ico.note{background:#f4d35a}
.info{position:absolute;left:335px;top:49px;width:392px;font-size:12.6px;line-height:14.3px}
.info h2{font-size:15.5px;font-weight:normal;margin-bottom:2px}
.info h3{font-size:13px;font-weight:bold}
.info p{margin-bottom:14.3px}
.info .ind{padding-left:13px}
.info .note{font-style:italic;font-size:10px;line-height:12px}
.thumbs{position:absolute;left:335px;top:490px;width:189px;height:83px;border:1px solid #333;border-radius:6px;box-shadow:1px 2px 3px rgba(0,0,0,.4);padding:4px 6px;display:flex;gap:4px}
.thumbs .fill{flex:1;border-radius:4px;background:radial-gradient(ellipse at 50% 55%,#333 0%,#777 50%,#e5e5e5 85%)}
.footer{position:absolute;left:0;top:748px;width:1200px;height:212px;background:linear-gradient(to bottom,#6f9fb3 0%,var(--sky-mid) 12%,var(--sky-light) 60%,var(--sky-light) 100%)}
.frame{position:absolute;left:128px;top:748px;width:953px;height:212px;border-left:1px solid #444;border-right:1px solid #444}
.divider{position:absolute;top:748px;width:1px;height:212px;background:#444}
.fhead{position:absolute;font-size:20px;color:#fff;text-shadow:1px 1px 2px #333;top:1px}
.flinks{position:absolute;list-style:none;font-size:12.5px;line-height:16px}
.flinks a{color:var(--navy);text-decoration:underline}
.search{position:absolute;left:868px;top:780px;display:flex;align-items:center;gap:3px}
.search .box{width:123px;height:18px;border:1px solid #222;border-radius:5px;background:#fff}
.search .go{font-size:19px;color:var(--navy);text-decoration:underline}
</style>
</head>
<body>
<header class="header">
  <div class="logo">Insert Logo Here...</div>
  <div class="tagline">Insert Tagline Here....</div>
</header>

<div class="stage"></div>

<aside class="sidebar">
  <ul class="nav">
    <li>Your Picks</li><li>Apparel</li><li>Auto</li><li>Awards &amp; Recognition</li><li>Bag&amp; Totes</li>
    <li>Bussiness Supplies</li><li>Calendars, Books &amp; Cards</li><li>Caps &amp; Hats</li><li>Clocks &amp; Watches</li>
    <li>Company Outings</li><li>Computer</li><li>Corprate Gifts</li><li>Desktop &amp; Office</li><li>Eco Friendly</li>
    <li>Electronics</li><li>Executive Gifts</li><li>Food, Candy, &amp; Drink</li><li>Games &amp; Novelties</li>
    <li>Gift Sets</li><li>Golf, Sports &amp; Outdoors</li>
  </ul>
</aside>

<div class="contact-bar"><b>Demo User</b> . <em>(555) 014-2273</em> . <a href="#">info@tondashop.example</a></div>

<main class="content">
  <h1 class="title">Tailgate Tote Cooler (TS# 518304)</h1>
  <a class="continue" href="#">Continue Shopping</a>

  <div class="photo"><div class="fill" role="img" aria-label="Product photo: black and silver cooler bag filled with snacks and drinks"></div></div>

  <div class="pricing">
    <div class="heads"><span>Quantity</span><span>Price</span></div>
    <div class="rows">
      <div>25<br>50<br>100<br>300</div>
      <div>$19.48<br>$16.75<br>$14.48<br>$13.98</div>
    </div>
  </div>

  <div class="actions">
    <div class="btn">REQUEST INFO<span class="ico note"></span></div>
    <div class="btn">ORDER SAMPLE<span class="ico"></span></div>
    <div class="btn">ADD TO CART<span class="ico"></span></div>
  </div>

  <section class="info">
    <h2>Product Information</h2>
    <h3>Tailgate Tote Cooler (TS#518304)</h3>
    <p>Bring the party wherever you go with this portable cooler. Lid with zipper keeps your beverages cold and your food fresh. 16"L opening Retractable metal bottle opener attached to bag. Heat sealed. 32 can capacity.<br>PEVA lining and PU fabric backing (non PVC).</p>
    <p>Fabric/Material: 210d polyester</p>
    <p>Size: 16"L 9.5"H 10"W<br>Imprint Area: Front pocket center 6.5W 3.5H</p>
    <p>Shipping Information:<br>Carton Size: 24"L 17"H 16"W<br>Quantity: 20<br>Weight: 26 lbs.</p>
    <h3>Price Includes</h3>
    <p class="ind">One Color/Location Silkscreen Imprint</p>
    <h3>Production Time *</h3>
    <p class="ind">5 - 7 Working Days</p>
    <h3>Setup Charge (per color)</h3>
    <p class="ind">$55.00</p>
    <h3>Available Colors</h3>
    <div class="ind">Black</div>
    <div class="note">* After credit, art and proof approval, excluding shipping time.</div>
  </section>

  <div class="thumbs">
    <div class="fill" role="img" aria-label="Thumbnail: cooler bag with snacks"></div>
    <div class="fill" role="img" aria-label="Thumbnail: cooler bag with bottles"></div>
  </div>
</main>

<footer class="footer">
  <div class="fhead" style="left:150px">Shop By Category</div>
  <ul class="flinks" style="left:150px;top:32px">
    <li><a>Apparel</a></li><li><a>Bags &amp; Totes</a></li><li><a>Caps &amp; Hats</a></li><li><a>Computer</a></li><li><a>Eco Friendly</a></li><li><a>Food, Candy &amp; Drink</a></li><li><a>Golf, Sports &amp; Outdoors</a></li><li><a>Home &amp; Housewares</a></li><li><a>Notebooks &amp; Folios</a></li><li><a>Tools &amp; Hardware</a></li><li><a>Writing Instruments</a></li>
  </ul>
  <ul class="flinks" style="left:328px;top:32px">
    <li><a>Auto</a></li><li><a>Business Supplies</a></li><li><a>Clocks &amp; Watches</a></li><li><a>Coporate Gifts</a></li><li><a>Electronics</a></li><li><a>Games &amp; Novelties</a></li><li><a>Healthcare &amp; Safety</a></li><li><a>Keychains</a></li><li><a>Pocket &amp; Purse</a></li><li><a>Tradeshows &amp; Events</a></li>
  </ul>
  <ul class="flinks" style="left:487px;top:32px">
    <li><a>Awards &amp; Recognition</a></li><li><a>Calendars, Books &amp; Cards</a></li><li><a>Company Outings</a></li><li><a>Desktop &amp; Office</a></li><li><a>Executive Gifts</a></li><li><a>Gift Sets</a></li><li><a>Holiday</a></li><li><a>Mugs &amp; Drinkware</a></li><li><a>Stress Balls &amp; Relievers</a></li><li><a>Travel &amp; luggage</a></li>
  </ul>
  <div class="fhead" style="left:705px">Shop By Price</div>
  <ul class="flinks" style="left:705px;top:32px">
    <li><a>Under $5</a></li><li><a>$5 - $10</a></li><li><a>$10 - $20</a></li><li><a>$20 - $50</a></li><li><a>$50 - $100</a></li><li><a>$100 - $200</a></li><li><a>Over $200</a></li>
  </ul>
  <div class="fhead" style="left:869px">Quick Search</div>
  <div class="fhead" style="left:869px;top:70px">Contact US</div>
  <ul class="flinks" style="left:869px;top:96px">
    <li><a>info@tondashop.example</a></li><li><a>www.tondashop.example</a></li>
  </ul>
</footer>
<div class="frame"></div>
<div class="divider" style="left:688px"></div>
<div class="divider" style="left:851px"></div>
<div class="search"><span class="box"></span><span class="go">Go</span></div>
</body>
</html>
```